Bathroom, Plumbing & TIling Business

I require a business card design for me new business the 'Ashgrove Tileworks Studio', based in Melbourne, Victoria.

Specialising in bathroom refurbishments, new installations, repairs, plumbing and tiling, the Ashgrove Tileworks Studio provides a professional high-quality standard of workmanship, creating your dream.

With over 15 years’ experience in the bathroom and plumbing industry the ATS will only take payment once the job is completed to the customers’ satisfaction*. We pride ourselves on hard-work, professionalism, customer service and always delivering that high end finish you have only dreamt of.

The majority of our work, to date, has come through personal recommendation and word-of-mouth and as a family-run company we do not pressure sell or push our customers to have unnecessary works.

The Ashgrove Tileworks Studio can source products for our customers at trade price and will always quote a job realistically, and honestly, on the work and materials required. We always let the customer know how long the job will take and we will complete it within the specified time.

ATS are dedicated to fitting new bathrooms, renovations, waterproofing, shower repairs/leaks and tiling to removing and refitting bathrooms, ensuites and showers and installing plumbing systems.

The business cards for ATS need to be clean, modern and simple. White matt finish with embossed bath logo.

On side 1 of the card we require the words 'Ashgrove Tileworks Studio' to be written in the Anson font with the letter V,B and C a lot larger in size to the other letters. The letter 'y' (at the end of the word 'Company') is to follow under the title in a curved bath shape growing up and around the letter V to a shower head dripping water in to the letter 'V' which will be half filled with water. The colour for the main title is the green colour which is used in the Waterfall colour scheme on MS Publisher. The tag line, 'Creating your Dream', is to be situated in a smaller font size, underneath the main title in the Anson font and be written in black (we think).

Side 2 of the card is to have a smaller sized version of the Side 1 logo (but only saying ATS - not the full title, Ashgrove Tileworks Studio) situated at the top and contact details (again, in the Anson font underneath.

The final design should communicate high-end, high quality and professionalism of bathroom fitting and plumbing works.
Updates

Hi there

Please could you include/list some of the services, provided by ATS on the back of the card:

Bathroom Renovations

Bathroom Installations

Tiling

Shower Repairs

Plumbing

Cheers :-)

Target Market(s)

Home owners, renters, property developers, rental companies seeking anything works related to bathrooms, plumbing and tiling. Age range from 21-70.

Industry/Entity Type

Industry

Requirements
Must have
• Double sided business card
Side 1: main - title (Ashgrove Tileworks Studio), logo (bath & shower) and tag line (Creating your Dream)
Side 2: Smaller sized version of Side 1 (but only with the letters ATS - not the whole company name) and contact details:

Rowan Pelliser (Owner)
Mordialloc, 3195

Website: www.ashgrovetileworksstudio.example
Email: Rowan@ats.example
Phone: +61 491 570 156
Nice to have
• The business cards for ATS need to be clean, modern and simple. White/or off white matt finish with embossed bath logo.

Should not have
• We do not want to see any of the following on the card:

No garish colours
No clip art
No cartoon images of people, baths or plumbing tools
No small photographs of bathrooms or other 'photographic' images

```html
<!DOCTYPE html>
<html lang="en">
<head>
<meta charset="utf-8">
<title>Ashgrove Tileworks Studio – Business Card</title>
<link rel="stylesheet" href="https://fonts.googleapis.com/css2?family=Dosis:wght@300;400&display=swap">
<style>
  :root {
    --brand-green: #5dbb9c;
    --ink: #1f1f1f;
    --paper: #ffffff;
    --on-band: #ffffff;
  }
  * { margin: 0; padding: 0; box-sizing: border-box; }
  html, body {
    width: 1200px;
    height: 686px;
    overflow: hidden;
    background: var(--paper);
  }
  .card {
    position: relative;
    width: 1200px;
    height: 686px;
    background: var(--paper);
    font-family: "Dosis", sans-serif;
    font-weight: 300;
  }
  .wordmark {
    position: absolute;
    left: 104px;
    top: 128px;
    font-size: 128px;
    line-height: 1;
    color: var(--brand-green);
    font-weight: 300;
    letter-spacing: 4px;
  }
  .services {
    position: absolute;
    right: 56px;
    top: 186px;
    text-align: center;
    color: var(--ink);
    font-size: 33px;
    line-height: 48px;
    letter-spacing: 0.5px;
  }
  .contact-band {
    position: absolute;
    left: 0;
    top: 442px;
    width: 1200px;
    height: 244px;
    background: var(--brand-green);
    color: var(--on-band);
  }
  .owner-name {
    position: absolute;
    left: 118px;
    top: 28px;
    font-size: 43px;
    letter-spacing: 0.5px;
  }
  .owner-role { font-size: 30px; }
  .contact-lines {
    position: absolute;
    right: 106px;
    top: 22px;
    text-align: right;
    font-size: 42px;
    line-height: 56px;
    letter-spacing: 0.5px;
  }
  .website {
    position: absolute;
    left: 114px;
    top: 140px;
    font-size: 51px;
    letter-spacing: 1.6px;
  }
</style>
</head>
<body>
  <div class="card">
    <div class="wordmark">ATS</div>

    <div class="services">
      <p>Bathroom Renovations &amp; Installations&#8226;Tiling</p>
      <p>Shower Repairs &#8226; Waterproofing &amp; Plumbing</p>
    </div>

    <div class="contact-band">
      <p class="owner-name">Rowan Pelliser <span class="owner-role">(Owner)</span></p>
      <div class="contact-lines">
        <p class="email">Rowan@ats.example</p>
        <p class="phone">+61 491 570 156</p>
      </div>
      <p class="website">www.ashgrovetileworksstudio.example</p>
    </div>
  </div>
</body>
</html>
```